NorthQuill.com Web Banner Design

NorthQuill.com is a national online business magazine that helps people in Canada start and grow their business. We have over 2000 articles, ask-the-expert answers and guides, as well as a free business directory.

We want to expand awareness for our site and need an exciting, promotional leaderboard and bigbox ad that is highly successful in getting people to click to visit our site, so the ads need to effectively create a sense of urgency. The two ads should share a consistent design and message.

The theme for this first ad group should be that anyone starting a business in Canada should come to NorthQuill for the answers they need to succeed. We are looking for creativity and the ads also need to be consistent with the NorthQuill brand.
Updates

Project Deadline Extended
Reason: Posting on the weekend seems to have limited the number of responses. We do design in house and are outsourcing this project because of time constraints - but we are looking for agency quality work. Check out examples from leading design blogs of great banner ad designs to get a feel for the quality we are looking for. Thank you!

Project Deadline Extended
Reason: Liking several of the designs and now just waiting for feedback from some of our advisors!

Project Deadline Extended
Reason: Still waiting for input, thank you for your patience. Also, for submissions that have a big box only, we are going to need to have a leaderboard version of the final design.

Target Market(s)

Canadians who or either starting a business or are running their own company with up to 25 staff. Some will be entrepreneurs with plans to grow to be a big company, others will want to make a living and don't want to grow. The common need is that they feel an urgency to get help and to get answers that will let them run their business effectively.

Requirements
Must have
• NorthQuill.com name, clearly branded
• NorthQuill logo (can be ad the end of the rotation of the ad)
• File size must be 150 kb or smaller
• Leaderboard size: 728 x90 pixels
• Big Box size: 250 x 250 pixels

```html
<!DOCTYPE html>
<html lang="en">
<head>
<meta charset="utf-8">
<title>NorthQuill.com Big Box Banners</title>
<link href="https://fonts.googleapis.com/css2?family=Open+Sans:wght@500;600;700;800&family=Exo:wght@700&display=swap" rel="stylesheet">
<style>
  :root {
    --board: #c9c9c9;
    --brand-blue: #0d80d9;
    --frame-blue: #1878c8;
    --cloud-back: #3a9de6;
    --cloud-white: #f4f4f4;
    --footer-grey: #f2f2f2;
    --button-green: #a3d21c;
    --button-green-dark: #86b80f;
    --button-text: #3b4a12;
    --logo-text: #4a6a8a;
    --white: #ffffff;
  }
  * { box-sizing: border-box; margin: 0; padding: 0; }
  html, body {
    width: 1200px; height: 750px; overflow: hidden;
    background: var(--board);
  }
  .board { position: relative; width: 1200px; height: 750px; }
  .banner {
    position: absolute;
    width: 250px; height: 250px;
    transform-origin: 0 0;
    transform: scale(1.171875);
    background: var(--brand-blue);
    border: 2px solid var(--frame-blue);
    overflow: hidden;
    font-family: "Open Sans", sans-serif;
    color: var(--white);
  }
  .banner--a { left: 334px; top: 55px; }
  .banner--b { left: 662px; top: 55px; }
  .banner--c { left: 334px; top: 386px; }
  .banner--d { left: 662px; top: 386px; }

  .headline {
    position: absolute; left: 0; right: 0; top: 16px;
    text-align: center;
    font-size: 24px; line-height: 30px; font-weight: 500;
    letter-spacing: -0.2px;
  }
  .headline strong { font-weight: 700; }

  .clouds { position: absolute; left: 0; top: 0; width: 250px; height: 250px; }

  .brand-mark {
    position: absolute; left: 14px; top: 180px;
    width: 90px; height: 52px;
    display: flex; align-items: center; justify-content: center; gap: 5px;
    font-size: 13px; font-weight: 600; color: var(--logo-text);
  }
  .brand-mark__dot {
    width: 9px; height: 9px; border-radius: 50%;
    background: var(--logo-text);
  }

  .cta {
    position: absolute; left: 119px; top: 192px;
    width: 110px; height: 36px;
    border-radius: 6px;
    background: linear-gradient(var(--button-green), var(--button-green-dark));
    color: var(--button-text);
    font-size: 13px; font-weight: 500;
    display: flex; align-items: center; justify-content: center; gap: 4px;
  }
  .cta strong { font-weight: 800; }

  .footer {
    position: absolute; left: 0; right: 0; top: 173px; bottom: 0;
    background: var(--footer-grey);
    display: flex; align-items: center; justify-content: center;
    font-family: "Exo", sans-serif;
    font-weight: 700; font-size: 19px; letter-spacing: 0.3px;
    color: var(--brand-blue);
  }
</style>
</head>
<body>
<main class="board">

  <section class="banner banner--a">
    <p class="headline">Get<br><strong>FREE HELP</strong><br>starting<br>your <strong>BUSINESS</strong></p>
    <svg class="clouds" viewBox="0 0 250 250" aria-hidden="true">
      <circle cx="12" cy="176" r="24" fill="var(--cloud-back)"/>
      <circle cx="232" cy="170" r="26" fill="var(--cloud-back)"/>
      <path d="M0 250V180Q22 160 48 170Q72 150 102 166Q128 152 152 164Q182 148 208 166Q232 158 250 172V250Z" fill="var(--cloud-white)"/>
    </svg>
    <div class="brand-mark"><span class="brand-mark__dot"></span>NorthQuill</div>
    <div class="cta">LEARN <strong>MORE</strong></div>
  </section>

  <section class="banner banner--b">
    <p class="headline"><strong>VISIT NOW</strong><br>to get the<br>information you<br><strong>need to SUCCEED</strong></p>
    <svg class="clouds" viewBox="0 0 250 250" aria-hidden="true">
      <circle cx="12" cy="176" r="24" fill="var(--cloud-back)"/>
      <circle cx="232" cy="170" r="26" fill="var(--cloud-back)"/>
      <path d="M0 250V180Q22 160 48 170Q72 150 102 166Q128 152 152 164Q182 148 208 166Q232 158 250 172V250Z" fill="var(--cloud-white)"/>
    </svg>
    <div class="brand-mark"><span class="brand-mark__dot"></span>NorthQuill</div>
    <div class="cta">LEARN <strong>MORE</strong></div>
  </section>

  <section class="banner banner--c">
    <p class="headline">Get<br><strong>FREE HELP</strong><br>starting<br>your <strong>BUSINESS</strong></p>
    <div class="footer">NORTHQUILL.COM</div>
  </section>

  <section class="banner banner--d">
    <p class="headline"><strong>VISIT NOW</strong><br>to get the<br>information you<br><strong>need to SUCCEED</strong></p>
    <div class="footer">NORTHQUILL.COM</div>
  </section>

</main>
</body>
</html>
```